Beach Polo Event Flyer

The project consists of a flyer for a beach polo event that will occur on August 30 and 31

The flyer should contain the event details in spanish:
IV MARENQUA SHORE RIDING CUP
Hotel Varlowe
Agosto 30 y 31 2014
Horario: 2pm a 6pm
(Varlowe Logo)

Also contact info below:
info@brisadelvarclub.example
www.brisadelvarclub.example

A Space should be left on the bottom for us to add the sponsor logos when we have them.

The general idea is to do a flyer that looks elegant, inviting, inspired on the beach and the caribbean and shows the beauty of the sport and the beach.

I am attaching the flyer that a friend made that we DO NOT LIKE and some flyers from events in other parts of the world that we do like.
Also attached you will find the BRISADEL VAR CLUB logo which should go somewhere in the flyer. We are also attaching pictures from the past event in case you would need to use them.
We are open for any questions

```html
<!DOCTYPE html>
<html lang="es">
<head>
<meta charset="utf-8">
<title>IV Marenqua Shore Riding Cup</title>
<link rel="stylesheet" href="https://fonts.googleapis.com/css2?family=Cinzel:wght@400;700&family=Libre+Baskerville&display=swap">
<style>
  :root {
    --sky-top: #2f7fcf;
    --sky-mid: #6aa8e0;
    --cloud: #c9dcef;
    --sea: #2a78a8;
    --sand: #c9b79b;
    --sand-dark: #a8957a;
    --white: #ffffff;
    --navy: #1f2a6b;
    --rule: #d8d8d8;
    --band: #1f86c4;
  }
  * { margin: 0; padding: 0; box-sizing: border-box; }
  html, body { width: 847px; height: 1200px; overflow: hidden; background: var(--white); }
  .flyer { position: relative; width: 847px; height: 1200px; background: var(--white); overflow: hidden; }

  .hero-photo {
    position: absolute; left: 0; top: 0; width: 847px; height: 866px;
    background: linear-gradient(180deg,
      var(--sky-top) 0%, var(--sky-mid) 45%, var(--cloud) 62%,
      var(--sea) 66%, var(--sea) 72%,
      var(--sand) 73%, var(--sand-dark) 100%);
  }

  .club-mark { position: absolute; top: 40px; left: 0; width: 100%; text-align: center; color: var(--white); }
  .club-mark .mark-circle { display: block; width: 62px; height: 62px; margin: 0 auto 6px; border: 2px solid var(--white); border-radius: 50%; }
  .club-mark .club-name { font-family: "Cinzel", serif; font-size: 12px; letter-spacing: 1px; }

  .event-title {
    position: absolute; top: 146px; left: 0; width: 100%; text-align: center;
    font-family: "Cinzel", serif; font-weight: 700; color: var(--white);
    font-size: 52px; line-height: 62px; letter-spacing: 1px;
  }

  .event-date {
    position: absolute; top: 276px; left: 142px; width: 562px;
    display: flex; align-items: center; gap: 14px;
    font-family: "Cinzel", serif; font-weight: 700; color: var(--white); font-size: 23px; white-space: nowrap;
  }
  .event-date .rule { flex: 1; height: 2px; background: var(--white); }

  .venue { position: absolute; top: 912px; left: 0; width: 847px; height: 86px; }
  .venue-text {
    position: absolute; right: 187px; top: 6px; text-align: right;
    font-family: "Libre Baskerville", serif; color: var(--navy); font-size: 25px; line-height: 38px;
  }
  .venue-divider { position: absolute; left: 680px; top: 0; width: 2px; height: 86px; background: var(--navy); }
  .venue-brand { position: absolute; left: 704px; top: 6px; width: 92px; text-align: center; color: var(--navy); }
  .venue-brand .brand-circle { display: block; width: 32px; height: 32px; margin: 0 auto 6px; border: 3px solid var(--navy); border-radius: 50%; }
  .venue-brand .brand-name { font-family: "Libre Baskerville", serif; font-size: 22px; }

  .sponsor-lines { position: absolute; left: 22px; width: 804px; height: 1px; background: var(--rule); }
  .sponsor-lines.first { top: 1042px; }
  .sponsor-lines.second { top: 1114px; }

  .contact-band {
    position: absolute; left: 0; top: 1164px; width: 847px; height: 36px; background: var(--band);
    color: var(--white); font-family: "Libre Baskerville", serif; font-size: 15px;
    display: flex; align-items: center; justify-content: center;
  }
</style>
</head>
<body>
<div class="flyer">
  <div class="hero-photo" role="img" aria-label="Photograph of polo players on horseback galloping along a sandy beach under a blue sky with the sea behind"></div>

  <div class="club-mark">
    <span class="mark-circle"></span>
    <span class="club-name">BRISADEL VAR CLUB</span>
  </div>

  <h1 class="event-title">IV MARENQUA<br>SHORE RIDING CUP</h1>

  <div class="event-date"><span class="rule"></span><span>Agosto 30 y 31 2014</span><span class="rule"></span></div>

  <div class="venue">
    <p class="venue-text">at Hotel Varlowe<br>Horario 2pm a 6pm</p>
    <span class="venue-divider"></span>
    <div class="venue-brand">
      <span class="brand-circle"></span>
      <span class="brand-name">Varlowe</span>
    </div>
  </div>

  <div class="sponsor-lines first"></div>
  <div class="sponsor-lines second"></div>

  <footer class="contact-band">info@brisadelvarclub.example &nbsp;|&nbsp; www.brisadelvarclub.example</footer>
</div>
</body>
</html>
```